Design a Cover for a Book on Innovation

I need a design for my book: The Quiet Orchard of Invention
It is about the following:

Innovation is not just for those endowed with special talent or skills in technology. This book describes the thought framework that consists of seven principal differences between the current period and the past. Innovation is happening along these shifts. Understanding the differences can allow for consistent innovation and the identification of real opportunities.
Updates

To All: All of you show great talent as designers. I've added a bit more to the description. Feel free to ask questions. Best, RT

Font styles to use
Sans Serif

Colors

Designer to choose colors to be used in the design.

Requirements
Must have
• It should feel modern and innovative. It should incorporate the meaning of Quiet Orchard.
Nice to have
• It should have the title, and a holder spot for the subtitle and author's name Rosa Ven Toh
Should not have
• It should not be overly busy. Sleek modern design that still gets the point across. Alternatively an image that is a full cover graphic.

```html
<!DOCTYPE html>
<html lang="en">
<head>
<meta charset="UTF-8">
<title>The Quiet Orchard of Invention — Book Cover</title>
<link rel="stylesheet" href="https://fonts.googleapis.com/css2?family=Lato:wght@400;700;900&display=swap">
<style>
  :root {
    --backdrop: #dfe5e8;
    --paper: #ffffff;
    --leaf-dark: #4f7a1e;
    --leaf-mid: #7fb03a;
    --leaf-light: #a9cf6a;
    --olive: #7a6a2a;
    --orange: #f08a1c;
    --orange-deep: #e2741a;
    --rule-green: #5fae2e;
    --ink: #4a4a4a;
    --ink-strong: #3c3c3c;
  }
  html, body {
    margin: 0;
    padding: 0;
    width: 1200px;
    height: 1200px;
    overflow: hidden;
    background: var(--backdrop);
  }
  .canvas {
    position: relative;
    width: 1200px;
    height: 1200px;
    font-family: "Lato", sans-serif;
  }
  .cover {
    position: absolute;
    left: 288px;
    top: 158px;
    width: 625px;
    height: 884px;
    background: var(--paper);
    box-shadow: 0 12px 30px rgba(60, 80, 90, 0.18);
    overflow: hidden;
  }
  .title {
    position: absolute;
    left: 85px;
    top: 78px;
    margin: 0;
    font-weight: 900;
    line-height: 1;
    text-transform: uppercase;
  }
  .title span { display: block; }
  .title-leaf {
    background: linear-gradient(160deg, var(--leaf-dark) 0%, var(--leaf-mid) 35%, var(--olive) 55%, var(--leaf-light) 75%, var(--leaf-dark) 100%);
    -webkit-background-clip: text;
    background-clip: text;
    color: transparent;
  }
  .title-kicker {
    font-size: 25px;
    letter-spacing: 0.5px;
  }
  .title-quiet {
    font-size: 128px;
    margin-top: 6px;
    letter-spacing: -2px;
  }
  .title-orchard {
    font-size: 96px;
    margin-top: 4px;
    letter-spacing: -2px;
  }
  .title-tail {
    font-size: 44px;
    margin-top: 14px;
    letter-spacing: -0.5px;
    background: linear-gradient(90deg, var(--orange-deep), var(--orange) 60%, #f5a23a);
    -webkit-background-clip: text;
    background-clip: text;
    color: transparent;
  }
  .title-rule {
    position: absolute;
    left: 0;
    top: 428px;
    width: 527px;
    height: 3px;
    background: var(--rule-green);
  }
  .subtitle {
    position: absolute;
    left: 89px;
    top: 448px;
    margin: 0;
    color: var(--ink);
    font-size: 20px;
    line-height: 31px;
  }
  .subtitle-lead {
    display: block;
    font-weight: 700;
    color: var(--ink-strong);
  }
  .produce-art {
    position: absolute;
    left: 65px;
    top: 560px;
    width: 496px;
    height: 190px;
    border-radius: 48% 48% 20% 20% / 60% 60% 20% 20%;
    background:
      radial-gradient(ellipse at 30% 60%, #c8402a 0%, transparent 40%),
      radial-gradient(ellipse at 70% 55%, #e2a83a 0%, transparent 45%),
      radial-gradient(ellipse at 50% 40%, #6f9a3a 0%, transparent 55%),
      linear-gradient(180deg, #8fb25a 0%, #b88a4a 60%, #d8c8a8 100%);
    opacity: 0.9;
  }
  .author {
    position: absolute;
    left: 0;
    right: 0;
    top: 790px;
    margin: 0;
    text-align: center;
    color: var(--orange);
    font-weight: 900;
    font-size: 44px;
    letter-spacing: 5px;
    text-transform: uppercase;
  }
</style>
</head>
<body>
<div class="canvas">
  <article class="cover">
    <h1 class="title">
      <span class="title-kicker title-leaf">The Quiet</span>
      <span class="title-quiet title-leaf">Quiet</span>
      <span class="title-orchard title-leaf">Orchard</span>
      <span class="title-tail">Of Invention</span>
    </h1>
    <div class="title-rule"></div>
    <p class="subtitle">
      <span class="subtitle-lead">Lorem Ipsum</span>
      In rhoncus bibendum ex at posuere.<br>
      Fusce viverra pulvinar risus in posuere.
    </p>
    <div class="produce-art" role="img" aria-label="Heaped fresh vegetables: tomatoes, eggplant, cauliflower, peppers, potatoes, garlic and corn"></div>
    <p class="author">Rosa Ven Toh</p>
  </article>
</div>
</body>
</html>
```